Corvallin Property Solutions need a business card design

Hello guys. We would need a business card design asap please.
We are a start up property investment business based in London UK specialised in buying, selling, managing and letting properties and helping distressed property owners.
The name of our Business is Corvallin, the logo symbolises the four fundamental elements of the world (earth, air, fire and water) and so it stands for strength, stability, longevity.
We would like the business card to communicate professionalism and reliability. Many many thanks indeed for your work.

Details:

1.) Marisol Dunkley
Property Investor
Mobile: +44(0)7700362517
Email: marisol.corvallin@quilbrook.example

2.) Tomas Brindle
Property Investor
Mobile: +44(0)7700845926
Email: tomas.corvallin@quilbrook.example

Industry/Entity Type

Investment

```html
<!DOCTYPE html>
<html lang="en">
<head>
<meta charset="utf-8">
<title>Corvallin Property Solutions – Business Card</title>
<link href="https://fonts.googleapis.com/css2?family=Jost:wght@600;700&family=Barlow:wght@400;500&display=swap" rel="stylesheet">
<style>
  :root {
    --stage: #2b2b2b;
    --caption: #c9c9c9;
    --card-white: #ffffff;
    --card-grey: #dedede;
    --band-light: #efedec;
    --band-dark: #d6d2d0;
    --band-edge: #c9c4c1;
    --ink: #111111;
    --accent-blue: #2c4f9e;
    --mark-fill: #2c4f9e;
    --icon-green: #2e9a48;
    --icon-red: #e0262f;
  }
  * { box-sizing: border-box; margin: 0; padding: 0; }
  html, body { width: 1000px; height: 1200px; overflow: hidden; }
  body { background: var(--stage); position: relative; font-family: "Barlow", Arial, sans-serif; }

  .card {
    position: absolute;
    width: 668px;
    height: 432px;
    background: linear-gradient(90deg, var(--card-white) 45%, var(--card-grey) 100%);
    overflow: hidden;
  }
  .card--front { left: 145px; top: 95px; }
  .card--back  { left: 155px; top: 651px; }

  .card__band { position: absolute; left: 0; top: 0; }

  .brand-mark {
    position: absolute;
    border-radius: 50%;
    background: var(--mark-fill);
  }
  .card--front .brand-mark { left: 120px; top: 110px; width: 140px; height: 140px; }
  .card--back .brand-mark  { left: 249px; top: 100px; width: 170px; height: 170px; }

  .wordmark { position: absolute; text-align: center; font-family: "Jost", "Futura", sans-serif; color: var(--ink); font-weight: 700; }
  .wordmark__name { display: block; text-transform: uppercase; letter-spacing: 0.5px; }
  .wordmark__tagline { display: block; text-transform: uppercase; font-weight: 700; }

  .card--front .wordmark { left: 70px; top: 282px; width: 240px; }
  .card--front .wordmark__name { font-size: 31px; line-height: 36px; }
  .card--front .wordmark__tagline { font-size: 15px; line-height: 20px; margin-top: 6px; }

  .card--back .wordmark { left: 134px; top: 292px; width: 400px; }
  .card--back .wordmark__name { font-size: 38px; line-height: 44px; }
  .card--back .wordmark__tagline { font-size: 18px; line-height: 24px; margin-top: 4px; }

  .contact { position: absolute; right: 48px; top: 160px; text-align: right; }
  .contact__name { font-family: "Jost", "Futura", sans-serif; font-weight: 600; font-size: 22px; letter-spacing: 0.8px; color: var(--ink); text-transform: uppercase; line-height: 26px; }
  .contact__role { font-size: 21px; color: var(--accent-blue); line-height: 26px; margin-top: 6px; }
  .contact__line { display: flex; justify-content: flex-end; align-items: center; gap: 7px; font-size: 15.5px; color: var(--ink); margin-top: 10px; }
  .contact__line--phone { margin-top: 24px; }
  .contact__line svg { display: block; }

  .caption { position: absolute; font-family: Arial, sans-serif; font-size: 20px; color: var(--caption); }
  .caption--front { left: 811px; top: 560px; }
  .caption--back  { left: 117px; top: 1144px; }
</style>
</head>
<body>

<section class="card card--front" aria-label="Business card front">
  <svg class="card__band" width="668" height="432" viewBox="0 0 668 432" aria-hidden="true">
    <defs>
      <linearGradient id="bandFill" x1="0" y1="0" x2="1" y2="1">
        <stop offset="0" stop-color="var(--band-dark)"/>
        <stop offset="0.5" stop-color="var(--band-light)"/>
        <stop offset="1" stop-color="var(--band-dark)"/>
      </linearGradient>
    </defs>
    <polygon points="0,0 150,0 395,432 0,432" fill="url(#bandFill)"/>
    <polygon points="150,0 160,0 405,432 395,432" fill="var(--band-edge)"/>
  </svg>

  <div class="brand-mark" aria-hidden="true"></div>
  <div class="wordmark">
    <span class="wordmark__name">Corvallin</span>
    <span class="wordmark__tagline">Property Solutions</span>
  </div>

  <div class="contact">
    <p class="contact__name">Marisol Dunkley</p>
    <p class="contact__role">Property Investor</p>
    <p class="contact__line contact__line--phone">+44(0)7700362517
      <svg width="14" height="22" viewBox="0 0 14 22" aria-hidden="true">
        <rect x="1" y="1" width="12" height="20" rx="2" fill="none" stroke="var(--icon-green)" stroke-width="2"/>
        <rect x="3.5" y="4" width="7" height="11" fill="var(--icon-green)" opacity="0.35"/>
        <circle cx="7" cy="18" r="1.2" fill="var(--icon-green)"/>
      </svg>
    </p>
    <p class="contact__line">marisol.corvallin@quilbrook.example
      <svg width="22" height="15" viewBox="0 0 22 15" aria-hidden="true">
        <rect x="0" y="0" width="22" height="15" fill="var(--icon-red)"/>
        <polyline points="1,1 11,9 21,1" fill="none" stroke="#fff" stroke-width="1.6"/>
        <line x1="1" y1="14" x2="8" y2="7" stroke="#fff" stroke-width="1.4"/>
        <line x1="21" y1="14" x2="14" y2="7" stroke="#fff" stroke-width="1.4"/>
      </svg>
    </p>
  </div>
</section>
<p class="caption caption--front">Front</p>

<section class="card card--back" aria-label="Business card back">
  <div class="brand-mark" aria-hidden="true"></div>
  <div class="wordmark">
    <span class="wordmark__name">Corvallin</span>
    <span class="wordmark__tagline">Property Solutions</span>
  </div>
</section>
<p class="caption caption--back">Back</p>

</body>
</html>
```